Harwick Electrical Business Card

create a simple but clear business card and letterhead - needs to be professional not too fancy and direct.

Target Market(s)

Home builders

Contact Information for Business Card

Information needed
Harwick Electrical Contracting
EC. No. 038275
Dario Pellegrin
Mobile 0427351186
dario@harwickelectrics.com.au

Requirements
Must have
• logo
• Harwick Electrical Contracting - H.E.D.
• EC. No. 038275
• Dario Pellegrin
• Mobile 0427351186
• dario@harwickelectrics.com.au
Nice to have
• black with white printing simple but clear
Should not have
• too much information
• no fancy writing

```html
<!DOCTYPE html>
<html lang="en">
<head>
<meta charset="utf-8">
<title>Harwick Electrical Contracting – Business Card</title>
<link rel="stylesheet" href="https://fonts.googleapis.com/css2?family=Exo+2:wght@700&family=Tinos:wght@700&display=swap">
<style>
  :root {
    --ink: #000000;
    --paper: #ffffff;
    --backdrop: #e8e6e2;
    --shadow: rgba(0, 0, 0, 0.18);
  }
  html, body {
    margin: 0;
    padding: 0;
    width: 1200px;
    height: 902px;
    overflow: hidden;
    background: var(--backdrop);
  }
  .canvas {
    position: relative;
    width: 1200px;
    height: 902px;
  }
  .business-card {
    position: absolute;
    left: 50px;
    top: 138px;
    width: 1100px;
    height: 626px;
    display: block;
    box-shadow: 0 10px 30px var(--shadow);
  }
  .card-ground { fill: var(--ink); }
  .card-swoosh { fill: var(--paper); }
  .brand-dot { fill: var(--ink); }
  .brand-name,
  .brand-tagline {
    font-family: "Exo 2", Arial, sans-serif;
    font-weight: 700;
    fill: var(--ink);
  }
  .brand-name { font-size: 50px; letter-spacing: 1px; }
  .brand-tagline { font-size: 26px; }
  .contact-name,
  .contact-line {
    font-family: "Tinos", "Times New Roman", serif;
    font-weight: 700;
    fill: var(--ink);
  }
  .contact-name { font-size: 34px; }
  .contact-line { font-size: 25px; }
  .icon-fill { fill: var(--ink); }
  .icon-stroke { fill: none; stroke: var(--paper); stroke-width: 1.6; }
</style>
</head>
<body>
<main class="canvas">
  <svg class="business-card" viewBox="0 0 940 535" xmlns="http://www.w3.org/2000/svg" aria-label="Harwick Electrical Contracting business card">
    <rect class="card-ground" x="0" y="0" width="940" height="535"/>
    <path class="card-swoosh" d="M0,205 C230,70 560,18 940,12 L940,212 C790,400 450,502 0,500 Z"/>

    <g class="brand">
      <circle class="brand-dot" cx="455" cy="137" r="72"/>
      <text class="brand-name" x="545" y="163">HARWICK</text>
      <text class="brand-tagline" x="545" y="196">Electrical Contracting</text>
    </g>

    <g class="contact">
      <text class="contact-name" x="38" y="313">Dario Pellegrin</text>

      <g class="icon-phone" transform="translate(38,352)">
        <path class="icon-fill" d="M0,7 C2,1 24,1 26,7 L26,10 L19,10 L19,7 L7,7 L7,10 L0,10 Z"/>
        <path class="icon-fill" d="M5,10 L21,10 L25,20 L1,20 Z"/>
        <circle class="icon-stroke" cx="13" cy="14.5" r="3"/>
      </g>
      <text class="contact-line" x="78" y="372">0427351186</text>

      <g class="icon-mail" transform="translate(38,392)">
        <rect class="icon-fill" x="0" y="0" width="26" height="18"/>
        <path class="icon-stroke" d="M1,1 L13,11 L25,1 M1,17 L10,8.5 M25,17 L16,8.5"/>
      </g>
      <text class="contact-line" x="78" y="409">dario@harwickelectrics.com.au</text>

      <text class="contact-line" x="40" y="468">EC. No. 038275</text>
    </g>
  </svg>
</main>
</body>
</html>
```